Bref créative
Edgy modern Letterhead an B. card for jet charter company
Veltaro Corporation
Professional
Peter Haldane
Founder, Chief Pilot
246 W. Harbor Ave., Suite 2020
Long Beach, CA 90815
855.5.VELTARO
phal@veltaro-example.com
veltaro-example.com
Use: Veltaro Corporation for company name

```html
<!DOCTYPE html>
<html lang="en">
<head>
<meta charset="utf-8">
<title>Veltaro Corporation – Business Card</title>
<link rel="stylesheet" href="https://fonts.googleapis.com/css2?family=Jost:wght@300;400&display=swap">
<style>
  :root {
    --stage: #1c1c1c;
    --ink: #0d0d0d;
    --paper: #ffffff;
    --paper-shade: #e9e9e9;
    --light-text: #f2f2f2;
    --dark-text: #111111;
    --muted: #bdbdbd;
  }
  * { margin: 0; padding: 0; box-sizing: border-box; }
  html, body { width: 1200px; height: 901px; overflow: hidden; }
  body {
    background: var(--stage);
    font-family: "Jost", sans-serif;
    position: relative;
  }
  .card {
    position: absolute;
    left: 250px;
    width: 700px;
    height: 400px;
    border-radius: 22px;
    overflow: hidden;
  }
  /* back face */
  .card-back {
    top: 33px;
    background: linear-gradient(135deg, #2a2a2a 0%, var(--ink) 45%, #000 100%);
  }
  .card-back .brand {
    position: absolute;
    left: 0; right: 0; top: 150px;
    text-align: center;
    color: var(--light-text);
    font-weight: 300;
    font-size: 78px;
    letter-spacing: 2px;
  }
  .card-back .web {
    position: absolute;
    right: 150px; top: 255px;
    color: var(--muted);
    font-size: 13px;
    letter-spacing: 1px;
  }
  /* front face */
  .card-front {
    top: 468px;
    background: linear-gradient(160deg, var(--paper) 55%, var(--paper-shade) 100%);
  }
  .card-front .shape { position: absolute; inset: 0; }
  .card-front .brand {
    position: absolute;
    left: 46px; top: 38px;
    color: var(--dark-text);
    font-weight: 300;
    font-size: 64px;
    letter-spacing: 1px;
  }
  .aircraft {
    position: absolute;
    left: 200px; top: 200px;
    width: 440px; height: 92px;
    border-radius: 40px 14px 46px 14px;
    background: linear-gradient(120deg, #2b2b2b, #0a0a0a);
  }
  .person {
    position: absolute;
    left: 470px; top: 146px;
    color: var(--dark-text);
  }
  .person .name { font-size: 17px; font-weight: 400; }
  .person .role { font-size: 12px; font-weight: 300; margin-top: 2px; }
  .contacts {
    position: absolute;
    left: 20px; top: 240px;
    list-style: none;
    color: var(--light-text);
    font-size: 13px;
    font-weight: 300;
    line-height: 19px;
  }
  .contacts li { display: flex; align-items: center; gap: 9px; }
  .contacts svg { width: 13px; height: 13px; fill: var(--light-text); }
  .address {
    position: absolute;
    left: 455px; top: 322px;
    color: var(--light-text);
    font-size: 14px;
    font-weight: 300;
    line-height: 18px;
  }
</style>
</head>
<body>

<section class="card card-back">
  <div class="brand">veltaro</div>
  <div class="web">veltaro-example.com</div>
</section>

<section class="card card-front">
  <svg class="shape" viewBox="0 0 700 400" aria-hidden="true">
    <path d="M0 230 Q0 212 18 212 L150 212 Q168 212 168 230 L168 318 Q330 338 700 300 L700 400 L0 400 Z" fill="#0d0d0d"/>
  </svg>

  <div class="brand">veltaro</div>

  <div class="aircraft" role="img" aria-label="Silhouette of a private jet in side view"></div>

  <div class="person">
    <div class="name">Peter Haldane</div>
    <div class="role">Founder, Chief Pilot</div>
  </div>

  <ul class="contacts">
    <li><svg viewBox="0 0 14 14"><path d="M3 1h2l1 3-1.5 1a7 7 0 0 0 4.5 4.5L10 8l3 1v2a2 2 0 0 1-2 2A10 10 0 0 1 1 3a2 2 0 0 1 2-2z"/></svg>855.5.VELTARO</li>
    <li><svg viewBox="0 0 14 14"><path d="M3 1h2l1 3-1.5 1a7 7 0 0 0 4.5 4.5L10 8l3 1v2a2 2 0 0 1-2 2A10 10 0 0 1 1 3a2 2 0 0 1 2-2z"/></svg>562.555.0130</li>
    <li><svg viewBox="0 0 14 14"><rect x="4" y="1" width="6" height="12" rx="1"/></svg>949.555.0177</li>
    <li><svg viewBox="0 0 14 14"><rect x="1" y="5" width="12" height="7" rx="1"/><rect x="3" y="1" width="8" height="4"/></svg>562.555.0131</li>
    <li><svg viewBox="0 0 14 14"><path d="M1 3h12v8H1z M1 3l6 5 6-5" stroke="#0d0d0d" stroke-width="1"/></svg>phal@veltaro-example.com</li>
  </ul>

  <div class="address">
    Veltaro Corporation<br>
    246 W. Harbor Ave., Suite 2020<br>
    Long Beach, CA 90815
  </div>
</section>

</body>
</html>
```